Create a Better Looking Excel Report

What I need is for the attached spreadsheet to be improved graphically. I would like it to utilise our branding from ([url removed, login to view]), for example a logo and contact details. What we need is a better looking report for the front-end of a very complex spreadsheet. The attached file is just the report in a workbook the winning style will be added to the actual working spreadsheet.

Please feel free to move around the tables and rearrange the data etc. The winning file format will be in .xls

Good luck!

```html
<!DOCTYPE html>
<html lang="en">
<head>
<meta charset="utf-8">
<title>Football Report</title>
<link href="https://fonts.googleapis.com/css2?family=Carlito:wght@400;700&display=swap" rel="stylesheet">
<style>
:root{
  --grid:#e2e2e2;
  --band-grey:#7f7f7f;
  --title-grey:#6b6b6b;
  --green:#a3d86f;
  --green-dark:#5f9a4f;
  --green-pale:#e0f5cb;
  --lime-line:#cfe8a8;
  --r1:#f2ef8d;
  --r2:#e9e98c;
  --r3:#e3dc90;
  --r4:#d9c672;
  --r5:#e2b566;
  --r6:#e8c98a;
  --r7:#f3cd7b;
  --r8:#f7e3b3;
  --ink:#1e1e1e;
  --white:#ffffff;
}
*{box-sizing:border-box;margin:0;padding:0}
html,body{width:1043px;height:1200px;overflow:hidden;background:var(--white)}
body{font-family:"Carlito",Calibri,Arial,sans-serif;color:var(--ink)}
.sheet{
  position:relative;width:900px;height:1035px;transform:scale(1.1589);transform-origin:0 0;
  background-image:
    repeating-linear-gradient(to bottom,transparent 0 21px,var(--grid) 21px 22px),
    repeating-linear-gradient(to right,transparent 0 55px,var(--grid) 55px 56px);
  background-position:0 5px;
}
.top-rule{position:absolute;left:0;top:0;width:893px;height:5px;background:var(--lime-line)}
.brand{position:absolute;left:30px;top:40px;display:flex;align-items:center;gap:10px;background:var(--white);padding:4px 6px}
.brand-mark{width:22px;height:22px;background:var(--green)}
.brand-name{font-size:27px;font-weight:700;color:#6f7880;letter-spacing:.5px}
.report-band{position:absolute;left:338px;top:5px;width:555px;height:100px;background:var(--band-grey);
  display:flex;align-items:center;justify-content:center;color:var(--white);font-weight:700;font-size:27px;letter-spacing:.5px}

.stats{position:absolute;left:0;width:620px;border-collapse:collapse;table-layout:fixed;font-size:12px}
.stats td,.stats th{height:22px;padding:0 4px;border:1px solid rgba(255,255,255,.55)}
.stats .season th{background:var(--title-grey);color:var(--white);text-align:left;font-weight:700;border:none}
.stats .head th{background:var(--green);font-weight:700;text-align:center}
.stats .total td{background:var(--green-dark);font-weight:700}
.stats .total td:first-child{color:var(--white)}
.stats .num{text-align:right}
.stats tbody td{border-color:rgba(0,0,0,.06)}
.row1 td{background:var(--r1)}.row2 td{background:var(--r2)}.row3 td{background:var(--r3)}.row4 td{background:var(--r4)}
.row5 td{background:var(--r5)}.row6 td{background:var(--r6)}.row7 td{background:var(--r7)}.row8 td{background:var(--r8)}

.contact{position:absolute;left:676px;top:138px;width:217px}
.contact-row{display:flex;height:44px;border-bottom:1px solid var(--white)}
.contact-icon{width:52px;background:var(--green-dark);display:flex;align-items:center;justify-content:center}
.contact-text{flex:1;background:var(--green-pale);display:flex;align-items:center;padding-left:6px;font-size:12px;white-space:nowrap}

.match-info{position:absolute;left:676px;top:336px;width:217px;border-collapse:collapse;font-size:12px}
.match-info td{height:22px;padding:0 5px;border-bottom:1px solid var(--white)}
.match-info .label{width:111px;background:var(--green);color:#eef6e4}
.match-info .value{background:var(--green-pale)}

.side-list{position:absolute;left:676px;width:217px;font-size:12px}
.side-title{background:var(--band-grey);color:var(--white);font-weight:700;height:22px;display:flex;align-items:center;justify-content:center}
.side-list li{list-style:none;height:22px;display:flex;align-items:center;padding-left:2px;border-bottom:1px solid rgba(255,255,255,.7)}
.key{top:446px}
.notes{top:688px}
.notes .side-title{height:65px;display:block;text-align:left;padding:6px 2px 0;font-size:12px}
.notes .side-title span{display:block;font-weight:400;line-height:1.3;width:170px}
.notes li{background:var(--green-pale)}
</style>
</head>
<body>
<div class="sheet">
  <div class="top-rule"></div>
  <div class="brand"><span class="brand-mark"></span><span class="brand-name">TAILORED SHEETS</span></div>
  <div class="report-band">FOOTBALL REPORT</div>

  <table class="stats" style="top:138px">
    <colgroup><col style="width:282px"><col style="width:113px"><col style="width:112px"><col style="width:113px"></colgroup>
    <thead>
      <tr class="season"><th colspan="4">Season 13-14</th></tr>
      <tr class="head"><th rowspan="2">Statistics to Display:</th><th colspan="3">Home/Away</th></tr>
      <tr class="head"><th>Ashford Vale</th><th>vs</th><th>Elmstead</th></tr>
    </thead>
    <tbody>
      <tr class="total"><td>Total Games</td><td class="num">11</td><td></td><td class="num">11</td></tr>
      <tr class="row1"><td>Over 2.5 Goals</td><td class="num">63.64%</td><td></td><td class="num">45.45%</td></tr>
      <tr class="row2"><td>Under 2.5 Goals</td><td class="num">36.36%</td><td></td><td class="num">54.55%</td></tr>
      <tr class="row3"><td>Under 10.5 Corners</td><td class="num">100%</td><td></td><td class="num">72.73%</td></tr>
      <tr class="row4"><td>Over 10.5 Corners</td><td class="num">0%</td><td></td><td class="num">27.27%</td></tr>
      <tr class="row5"><td>Both to Score</td><td class="num">36.36%</td><td></td><td class="num">45.45%</td></tr>
      <tr class="row6"><td>Win %</td><td class="num">18.18%</td><td></td><td class="num">63.64%</td></tr>
      <tr class="row7"><td>Half Time Win %</td><td class="num">0%</td><td></td><td class="num">54.55%</td></tr>
      <tr class="row8"><td>Over 1.5 Team Goals</td><td class="num">18.18%</td><td></td><td class="num">63.64%</td></tr>
    </tbody>
  </table>

  <table class="stats" style="top:448px">
    <colgroup><col style="width:282px"><col style="width:113px"><col style="width:112px"><col style="width:113px"></colgroup>
    <thead>
      <tr class="season"><th colspan="4">Season 12-13</th></tr>
      <tr class="head"><th rowspan="2">Statistics to Display:</th><th colspan="3">Home/Away</th></tr>
      <tr class="head"><th>Ashford Vale</th><th>vs</th><th>Elmstead</th></tr>
    </thead>
    <tbody>
      <tr class="total"><td>Total Games</td><td class="num">19</td><td></td><td class="num">19</td></tr>
      <tr class="row1"><td>Over 2.5 Goals</td><td class="num">47.4%</td><td></td><td class="num">47.37%</td></tr>
      <tr class="row2"><td>Under 2.5 Goals</td><td class="num">52.6%</td><td></td><td class="num">52.63%</td></tr>
      <tr class="row3"><td>Under 10.5 Corners</td><td class="num">89.5%</td><td></td><td class="num">94.74%</td></tr>
      <tr class="row4"><td>Over 10.5 Corners</td><td class="num">10.5%</td><td></td><td class="num">5.26%</td></tr>
      <tr class="row5"><td>Both to Score</td><td class="num">57.9%</td><td></td><td class="num">63.16%</td></tr>
      <tr class="row6"><td>Win %</td><td class="num">26.3%</td><td></td><td class="num">21.05%</td></tr>
      <tr class="row7"><td>Half Time Win %</td><td class="num">31.6%</td><td></td><td class="num">26.32%</td></tr>
      <tr class="row8"><td>Over 1.5 Team Goals</td><td class="num">26.3%</td><td></td><td class="num">36.84%</td></tr>
    </tbody>
  </table>

  <table class="stats" style="top:755px">
    <colgroup><col style="width:282px"><col style="width:113px"><col style="width:112px"><col style="width:113px"></colgroup>
    <thead>
      <tr class="season"><th colspan="4">Season 11-12</th></tr>
      <tr class="head"><th rowspan="2">Statistics to Display:</th><th colspan="3">Home/Away</th></tr>
      <tr class="head"><th>Ashford Vale</th><th>vs</th><th>Elmstead</th></tr>
    </thead>
    <tbody>
      <tr class="total"><td>Total Games</td><td class="num">19</td><td></td><td class="num">19</td></tr>
      <tr class="row1"><td>Over 2.5 Goals</td><td class="num">63.2%</td><td></td><td class="num">68.4%</td></tr>
      <tr class="row2"><td>Under 2.5 Goals</td><td class="num">36.8%</td><td></td><td class="num">31.6%</td></tr>
      <tr class="row3"><td>Under 10.5 Corners</td><td class="num">89.5%</td><td></td><td class="num">100.0%</td></tr>
      <tr class="row4"><td>Over 10.5 Corners</td><td class="num">10.5%</td><td></td><td class="num">0.0%</td></tr>
      <tr class="row5"><td>Both to Score</td><td class="num">57.9%</td><td></td><td class="num">52.6%</td></tr>
      <tr class="row6"><td>Win %</td><td class="num">21.1%</td><td></td><td class="num">26.3%</td></tr>
      <tr class="row7"><td>Half Time Win %</td><td class="num">26.3%</td><td></td><td class="num">10.5%</td></tr>
      <tr class="row8"><td>Over 1.5 Team Goals</td><td class="num">26.3%</td><td></td><td class="num">26.3%</td></tr>
    </tbody>
  </table>

  <div class="contact">
    <div class="contact-row">
      <div class="contact-icon"><svg width="24" height="18" viewBox="0 0 24 18"><rect x="1" y="1" width="22" height="16" fill="none" stroke="#fff" stroke-width="2"/><path d="M1 1 L12 10 L23 1" fill="none" stroke="#fff" stroke-width="2"/></svg></div>
      <div class="contact-text">support@tailored-sheets.co</div>
    </div>
    <div class="contact-row">
      <div class="contact-icon"><svg width="22" height="22" viewBox="0 0 24 24"><path d="M6.6 10.8c1.4 2.8 3.8 5.1 6.6 6.6l2.2-2.2c.3-.3.7-.4 1-.2 1.1.4 2.3.6 3.6.6.6 0 1 .4 1 1V20c0 .6-.4 1-1 1C10.6 21 3 13.4 3 4c0-.6.4-1 1-1h3.5c.6 0 1 .4 1 1 0 1.3.2 2.5.6 3.6.1.3 0 .7-.2 1z" fill="#fff"/></svg></div>
      <div class="contact-text">0161 555 0142</div>
    </div>
    <div class="contact-row">
      <div class="contact-icon"><svg width="22" height="22" viewBox="0 0 22 22"><circle cx="11" cy="11" r="9" fill="#fff"/></svg></div>
      <div class="contact-text">Chat ID: tailored.sheets</div>
    </div>
    <div class="contact-row">
      <div class="contact-icon"><svg width="22" height="22" viewBox="0 0 22 22"><circle cx="11" cy="11" r="9" fill="#fff"/></svg></div>
      <div class="contact-text">Follow Us</div>
    </div>
  </div>

  <table class="match-info">
    <tr><td class="label">League</td><td class="value">Top Flight</td></tr>
    <tr><td class="label">Home Team</td><td class="value">Ashford Vale</td></tr>
    <tr><td class="label">Away Team</td><td class="value">Elmstead</td></tr>
  </table>

  <div class="side-list key">
    <div class="side-title">Formatting Key</div>
    <ul>
      <li style="background:var(--r1)">Over 2.5 Goals</li>
      <li style="background:var(--r2)">Under 2.5 Goals</li>
      <li style="background:var(--r3)">Under 10.5 Corners</li>
      <li style="background:var(--r4)">Over 10.5 Corners</li>
      <li style="background:var(--r5)">Both to Score</li>
      <li style="background:var(--r6)">Win %</li>
      <li style="background:var(--r7)">Half Time Win %</li>
      <li style="background:var(--r8)">Over 1.5 Team Goals</li>
    </ul>
  </div>

  <div class="side-list notes">
    <div class="side-title">Notes<span>Please be aware there is no information for corners in the following leagues:</span></div>
    <ul>
      <li>Northern Championship</li>
      <li>Northern 2nd Division</li>
      <li>Northern 3rd Division</li>
      <li>Southern Second</li>
      <li>Central League 2</li>
      <li>Coastal Series B</li>
      <li>Western League 2</li>
      <li>Lowland Division</li>
      <li>Island Super League</li>
      <li>Harbour League</li>
      <li>Eastern Liga</li>
      <li>Valley Pro League</li>
    </ul>
  </div>
</div>
</body>
</html>
```